Sphynx Cat Breeder

Hi.
I have just got a logo through Pixel Harbor, and now I need a website.
I am home based Sphynx cat breeder (Plumwick Sphynx)
I want to be able to show my breedings cats and kittens available for sale on my website.

Target Market(s)

Buyers of pet kittens in New Zealand, plus potentially buyers of kittens for breeding for overseas breeders

Requirements
Must have
• Home page
About Us
My breeding Cats
Kittens
Caring for a Sphynx
Links
Contact (contact details plus a link to email)
I need to be able to upload photos as kittens come and go.
Nice to have
• A web counter, visible only to me, preferably showing which country they are from

```html
<!DOCTYPE html>
<html lang="en">
<head>
<meta charset="utf-8">
<title>Plumwick Sphynx</title>
<link rel="stylesheet" href="https://fonts.googleapis.com/css2?family=Arimo:wght@400;700&family=Roboto+Slab:wght@300;400&family=Mulish:wght@400&family=Gelasio:ital,wght@1,400&display=swap">
<style>
  :root {
    --nav-bg: #121415;
    --nav-text: #e4e4e4;
    --page-bg: #eeeeee;
    --ink: #2a2a2a;
    --body-text: #2f2f2f;
    --rule: #d9d9d9;
    --link: #1a98d5;
    --button: #1f9de0;
    --field-border: #c9c9c9;
    --footer-top: #1a2527;
    --footer-bottom: #050809;
  }
  * { margin: 0; padding: 0; box-sizing: border-box; }
  html, body { width: 1200px; height: 1140px; overflow: hidden; }
  body {
    position: relative;
    background: var(--page-bg);
    font-family: "Arimo", Arial, sans-serif;
    color: var(--body-text);
  }
  .top-bar {
    position: absolute; left: 0; top: 0; width: 1200px; height: 75px;
    background: radial-gradient(ellipse 420px 60px at 560px 75px, #2a3c40 0%, var(--nav-bg) 70%);
  }
  .main-nav {
    position: absolute; left: 169px; top: 28px;
    display: flex; gap: 16px; list-style: none;
    font-weight: 700; font-size: 15px; color: var(--nav-text);
  }
  .header-band {
    position: absolute; left: 0; top: 75px; width: 1200px; height: 357px;
    background: linear-gradient(#f6f6f6, #ececec);
  }
  .brand {
    position: absolute; left: 176px; top: 226px;
    font-family: "Mulish", sans-serif; font-size: 24px; line-height: 30px; color: #1b1b1b;
  }
  .contact-lines {
    position: absolute; right: 176px; top: 208px; text-align: right;
    font-family: "Mulish", sans-serif; font-size: 28px; line-height: 33px; color: var(--ink);
  }
  .banner {
    position: absolute; left: 168px; top: 277px; width: 858px; height: 239px;
    background: #fff; padding: 7px 6px;
    box-shadow: 0 30px 22px -18px rgba(0,0,0,0.45);
  }
  .banner-photo {
    width: 100%; height: 100%;
    background: linear-gradient(90deg, #8fb0e2 0%, #b9c6dc 40%, #9bb4e0 70%, #cfdaf0 100%);
  }
  .about { position: absolute; left: 176px; top: 580px; width: 592px; }
  .about h1 {
    font-family: "Roboto Slab", serif; font-weight: 400; font-size: 28px;
    color: var(--ink); margin-top: 2px; margin-bottom: 14px;
  }
  .about p { font-size: 12.2px; line-height: 15.2px; margin-bottom: 16px; }
  .quote {
    position: relative; border-top: 1px solid var(--rule); border-bottom: 1px solid var(--rule);
    margin-top: 20px; padding: 18px 0 18px 71px; height: 113px;
  }
  .quote-mark {
    position: absolute; left: 0; top: 11px; width: 60px; height: 60px;
    border-radius: 50%; border: 4px solid #dadada; background: #ececec;
  }
  .quote p {
    font-family: "Gelasio", Georgia, serif; font-style: italic; font-weight: 400;
    font-size: 12.2px; line-height: 15.2px; margin-bottom: 17px; color: #333;
  }
  .dot { font-size: 10px; margin-top: 6px; }
  .column-rule { position: absolute; left: 794px; top: 580px; width: 1px; height: 336px; background: var(--rule); }
  .blog { position: absolute; left: 816px; top: 586px; width: 213px; }
  .blog h2 {
    font-family: "Roboto Slab", serif; font-weight: 400; font-size: 18px;
    color: var(--ink); padding-bottom: 9px; border-bottom: 1px solid var(--rule);
  }
  .blog ul { list-style: none; }
  .blog li {
    font-size: 11.8px; line-height: 15px; color: var(--link);
    padding: 6px 0 5px; border-bottom: 1px solid var(--rule);
  }
  .blog li:last-child { border-bottom: none; }
  .contact-band {
    position: absolute; left: 0; top: 923px; width: 1200px; height: 153px;
    border-top: 1px solid #d2d2d2; background: #f2f2f2;
  }
  .hide-tab {
    position: absolute; left: 981px; top: -2px; width: 40px; height: 14px;
    background: var(--button); color: #fff; font-size: 7px; text-align: center; line-height: 13px;
    border-radius: 0 0 5px 5px;
  }
  .mail-icon { position: absolute; left: 194px; top: 32px; }
  .field {
    position: absolute; left: 268px; width: 135px; height: 25px;
    background: linear-gradient(#dadada, #ececec); border: 1px solid var(--field-border); border-radius: 3px;
    font-size: 11px; color: #555; padding: 6px 8px;
  }
  .send {
    position: absolute; left: 333px; top: 96px; width: 71px; height: 21px;
    background: linear-gradient(#4fbaf0, var(--button)); border-radius: 4px;
    color: #fff; font-weight: 700; font-size: 11.5px; text-align: center; line-height: 21px;
  }
  .message {
    position: absolute; left: 414px; top: 31px; width: 608px; height: 91px;
    background: linear-gradient(#f4f4f4 40%, #dedede); border: 1px solid var(--field-border); border-radius: 3px;
    font-size: 11px; color: #555; padding: 5px 7px;
  }
  .site-footer {
    position: absolute; left: 0; top: 1076px; width: 1200px; height: 64px;
    background: linear-gradient(var(--footer-top), var(--footer-bottom));
    color: #fff; font-size: 12.5px; text-align: center; padding-top: 11px; padding-left: 104px;
  }
</style>
</head>
<body>
  <header>
    <div class="top-bar">
      <ul class="main-nav">
        <li>Home</li><li>About Us</li><li>My breeding Cats</li><li>Kittens</li>
        <li>Caring for a Sphynx</li><li>Links</li><li>Contact</li>
      </ul>
    </div>
    <div class="header-band"></div>
    <div class="brand">Plumwick Sphynx</div>
    <div class="contact-lines">
      <div>Phone (000) 1234 567</div>
      <div>Email info@plumwicksphynx.com</div>
    </div>
    <div class="banner">
      <div class="banner-photo" role="img" aria-label="Photo of a group of Sphynx kittens on a blue backdrop"></div>
    </div>
  </header>

  <main>
    <section class="about">
      <h1>About</h1>
      <p>Lorem ipsum dolor sit amet, consectetur adipisicing elit, sed do eiusmod tempor incididunt ut labore et dolore magna aliqua. Lorem ipsum dolor sit amet, consectetur adipisicing elit, sed do eiusmod tempor incididunt ut labore et dolore magna aliqua.[/col2]</p>
      <p>Lorem ipsum dolor sit amet, consectetur adipisicing elit, sed do eiusmod tempor incididunt ut labore et dolore magna aliqua. Lorem ipsum dolor sit amet, consectetur adipisicing elit, sed do eiusmod tempor incididunt ut labore et dolore magna aliqua.Lorem ipsum dolor sit amet, consectetur adipisicing elit, sed do eiusmod tempor incididunt ut labore et dolore magna aliqua.Lorem ipsum dolor sit amet, consectetur adipisicing elit, sed do eiusmod tempor incididunt ut labore et dolore magna aliqua.</p>
      <blockquote class="quote">
        <div class="quote-mark"></div>
        <p>This is a blockquote!</p>
        <p>Lorem ipsum dolor sit amet, consectetur adipisicing elit, sed do eiusmod tempor incididunt ut labore et dolore magna aliqua. Lorem ipsum dolor sit amet, consectetur adipisicing elit, sed do eiusmod tempor incididunt ut labore et dolore magna aliqua.</p>
      </blockquote>
      <div class="dot">.</div>
    </section>

    <div class="column-rule"></div>

    <aside class="blog">
      <h2>Lates Blog Entries</h2>
      <ul>
        <li>Tempor incididunt ut labore et</li>
        <li>Tempor incididunt ut labore et</li>
        <li>Tempor incididunt ut labore et</li>
        <li>Tempor incididunt ut labore et</li>
        <li>Nam libero tempore, cum soluta nobis est</li>
        <li>Tempor incididunt ut labore et</li>
        <li>Tempor incididunt ut labore et</li>
        <li>Tempor incididunt ut labore et</li>
        <li>Tempor incididunt ut labore et</li>
        <li>Nam libero tempore, cum soluta nobis est</li>
      </ul>
    </aside>
  </main>

  <section class="contact-band">
    <div class="hide-tab">hide</div>
    <svg class="mail-icon" width="54" height="50" viewBox="0 0 54 50">
      <rect x="1" y="14" width="52" height="34" fill="#9cc6ee" stroke="#5d93c9"/>
      <polygon points="1,14 27,0 53,14 27,30" fill="#f5c21b" stroke="#d49a10"/>
      <polyline points="1,48 27,28 53,48" fill="none" stroke="#5d93c9"/>
    </svg>
    <div class="field" style="top:31px">your name</div>
    <div class="field" style="top:62px">your email</div>
    <div class="send">Send</div>
    <div class="message">your message</div>
  </section>

  <footer class="site-footer">3434345 Visitors</footer>
</body>
</html>
```